| ■お仕事内容 海外の高級ファッションブランドを販売するサイト用の無償修理保証のバナー製作をお願いいたします。 メンズ、レディースどちらも取り扱っているブランドのため、どちらでも使えるデザインが望ましいです。 ■バナーに記載する内容 「1年間無償修理保証」ということが伝わる文章を入れてください。 ※独自のサービスのため、「当店だけの・・・」など独自の付加価値サービスである文言を入れたいです。 ■重視する点 ・高級感のあるデザイン(ごちゃごちゃしていない、シンプルで目を引くもの) ・フラットデザインが基調になっているサイトにマッチするデザイン ・ファッション系のサイトに合うデザイン ・本物である安心感・信頼感のあるデザイン ■報酬 5,000円 ■応募条件 WEBサイトのバナー、アイコンなどの製作経験をお持ちの方 ご提案価格と実績のバランスを見てお仕事をお願いする方を選定させていただきます。 たくさんのご応募お待ちしております。 何卒宜しくお願いいたします。 |

```html
<!DOCTYPE html>
<html lang="ja">
<head>
<meta charset="UTF-8">
<title>1年間無償修理保証 バナー</title>
<link href="https://fonts.googleapis.com/css2?family=Noto+Serif+JP:wght@400;500;600&display=swap" rel="stylesheet">
<style>
  :root {
    --ink-dark: #140b03;
    --bronze-deep: #3a2006;
    --bronze: #7a4a0c;
    --gold: #d99a1c;
    --gold-bright: #ffd35a;
    --gold-pale: #ffe9a6;
    --line-gold: #c8922a;
    --text-white: #ffffff;
    --text-cream: #f6ecd8;
  }
  html, body {
    margin: 0;
    padding: 0;
    width: 1200px;
    height: 188px;
    overflow: hidden;
    background: #000;
  }
  .banner {
    position: relative;
    width: 1200px;
    height: 188px;
    overflow: hidden;
    background:
      linear-gradient(115deg, transparent 0 52%, rgba(255,225,120,0.35) 55%, transparent 60%),
      linear-gradient(115deg, transparent 0 63%, rgba(255,210,100,0.25) 66%, transparent 70%),
      linear-gradient(115deg, transparent 0 74%, rgba(255,200,90,0.18) 77%, transparent 82%),
      radial-gradient(ellipse 420px 200px at 720px 110px, rgba(255,214,90,0.95), rgba(217,154,28,0.7) 45%, transparent 80%),
      linear-gradient(90deg, var(--ink-dark) 0%, #22130a 18%, var(--bronze-deep) 32%, var(--bronze) 45%, var(--gold) 58%, var(--bronze) 75%, var(--bronze-deep) 88%, #24150a 100%);
  }
  .rule {
    position: absolute;
    left: 0;
    width: 1200px;
    height: 2px;
    background: linear-gradient(90deg, #5a3a10, var(--line-gold) 30%, var(--gold-pale) 60%, var(--line-gold) 85%, #5a3a10);
  }
  .rule--top { top: 5px; }
  .rule--bottom { bottom: 5px; }
  .tagline {
    position: absolute;
    left: 46px;
    top: 14px;
    margin: 0;
    font-family: "Noto Serif JP", serif;
    font-weight: 500;
    font-size: 27px;
    letter-spacing: 1px;
    color: var(--text-cream);
    text-shadow: 0 1px 2px rgba(0,0,0,0.8);
  }
  .headline {
    position: absolute;
    left: 40px;
    top: 52px;
    margin: 0;
    font-family: "Noto Serif JP", serif;
    font-weight: 500;
    font-size: 78px;
    line-height: 1.2;
    letter-spacing: 3px;
    color: var(--text-white);
    white-space: nowrap;
    text-shadow: 2px 3px 3px rgba(40,20,0,0.85), 0 0 8px rgba(0,0,0,0.5);
  }
  .headline .num { margin-right: 22px; }
</style>
</head>
<body>
  <div class="banner">
    <div class="rule rule--top"></div>
    <p class="tagline">当店だから、このサービス</p>
    <h1 class="headline"><span class="num">1</span>年間無償修理保証</h1>
    <div class="rule rule--bottom"></div>
  </div>
</body>
</html>
```